hi all

Im after a new age looking business card with my company logo on it

must include these details, I would like the PH and Email to be symbols

If the colours used for card could be kept within the colours used in logo that I have supplied that would be great, if another colour is to be used dark grey would be ok. no light bulbs etc thanks

Details below to be incorporated on card

Damian Holloway

Lic E871302

PH 0219647381

E info@brightvaleelectrical.example.nz

Domestic Commercial Industrial Electricians

```html
<!DOCTYPE html>
<html lang="en">
<head>
<meta charset="utf-8">
<title>Brightvale Electrical – Business Card</title>
<link href="https://fonts.googleapis.com/css2?family=Montserrat:wght@400;500;600;700;800&display=swap" rel="stylesheet">
<style>
  :root {
    --backdrop: #8a8d8b;
    --brand-blue: #0b6aab;
    --brand-blue-deep: #0a5f9c;
    --ink: #1f2326;
    --paper: #f7f7f6;
    --ghost: #e9eaea;
    --white: #ffffff;
  }
  * { margin: 0; padding: 0; box-sizing: border-box; }
  html, body {
    width: 1200px; height: 866px; overflow: hidden;
    background: var(--backdrop);
    font-family: "Montserrat", sans-serif;
  }
  .canvas {
    position: relative; width: 1200px; height: 866px;
    display: flex; align-items: center; justify-content: center; gap: 40px;
  }
  .card {
    position: relative; width: 525px; height: 300px; overflow: hidden;
    box-shadow: 0 10px 24px rgba(0,0,0,.28);
  }

  /* Front */
  .card-front { background: var(--brand-blue); }
  .circuit-art {
    position: absolute; left: 40px; top: 10px; width: 420px; height: 240px;
    background: radial-gradient(ellipse at 60% 45%, rgba(255,255,255,.14), rgba(255,255,255,0) 70%);
  }
  .front-brand {
    position: absolute; left: 0; right: 0; top: 92px;
    display: flex; flex-direction: column; align-items: center; gap: 14px;
  }
  .brand-dot {
    width: 58px; height: 58px; border-radius: 50%; background: var(--white);
  }
  .front-brand .brand-name {
    color: var(--white); font-weight: 800; font-size: 34px; letter-spacing: 2px;
    text-transform: uppercase; line-height: 1;
  }
  .services-band {
    position: absolute; left: 0; right: 0; bottom: 22px; height: 34px;
    background: linear-gradient(90deg, var(--white) 0%, var(--white) 80%, rgba(255,255,255,.5) 100%);
    display: flex; align-items: center; justify-content: center;
    color: var(--brand-blue); font-weight: 600; font-size: 13px; letter-spacing: 2.4px;
    text-transform: uppercase; white-space: nowrap;
  }

  /* Back */
  .card-back { background: var(--paper); }
  .ghost-name {
    position: absolute; color: var(--ghost); font-weight: 800; font-size: 92px;
    letter-spacing: 4px; line-height: 1; text-transform: uppercase; white-space: nowrap;
  }
  .ghost-first { top: -34px; left: 60px; }
  .ghost-last { bottom: -40px; left: 40px; }
  .back-brand {
    position: absolute; left: 26px; top: 122px;
    display: flex; align-items: center; gap: 9px;
  }
  .back-brand .brand-dot { width: 20px; height: 20px; background: var(--brand-blue); }
  .back-brand .brand-name {
    color: var(--brand-blue); font-weight: 800; font-size: 17px; letter-spacing: 1px;
    text-transform: uppercase; line-height: 1.1;
  }
  .contact {
    position: absolute; left: 204px; right: 14px; top: 96px; color: var(--ink);
  }
  .contact-name {
    color: var(--brand-blue); font-weight: 700; font-size: 17px; letter-spacing: .5px;
    text-transform: uppercase; white-space: nowrap;
  }
  .contact-licence { font-size: 14px; margin-top: 4px; }
  .contact-rule { width: 18px; height: 2px; background: var(--brand-blue); margin: 14px 0 12px; }
  .contact-line {
    display: flex; align-items: center; gap: 8px; font-size: 12.5px;
    margin-bottom: 8px; white-space: nowrap;
  }
  .contact-line svg { width: 14px; height: 14px; flex: none; }
</style>
</head>
<body>
<main class="canvas">

  <section class="card card-front">
    <div class="circuit-art" role="img" aria-label="Faint circuit diagram line art"></div>
    <div class="front-brand">
      <span class="brand-dot"></span>
      <span class="brand-name">Brightvale Electrical</span>
    </div>
    <div class="services-band">Domestic • Commercial • Industrial • Electricians</div>
  </section>

  <section class="card card-back">
    <span class="ghost-name ghost-first" aria-hidden="true">Damian</span>
    <span class="ghost-name ghost-last" aria-hidden="true">Holloway</span>

    <div class="back-brand">
      <span class="brand-dot"></span>
      <span class="brand-name">Brightvale<br>Electrical</span>
    </div>

    <div class="contact">
      <p class="contact-name">Damian Holloway</p>
      <p class="contact-licence">Lic E871302</p>
      <div class="contact-rule"></div>
      <p class="contact-line">
        <svg viewBox="0 0 24 24" fill="none" stroke="#0b6aab" stroke-width="2"><path d="M5 3h4l2 5-3 2a11 11 0 0 0 6 6l2-3 5 2v4a2 2 0 0 1-2 2A17 17 0 0 1 3 5a2 2 0 0 1 2-2z"/></svg>
        0219 647 381
      </p>
      <p class="contact-line">
        <svg viewBox="0 0 24 24" fill="none" stroke="#0b6aab" stroke-width="2"><rect x="3" y="5" width="18" height="14" rx="1"/><path d="M3 6l9 7 9-7"/></svg>
        info@brightvaleelectrical.example.nz
      </p>
    </div>
  </section>

</main>
</body>
</html>
```